Equity, Effectiveness and Efficiency in charitable food relief sector

I am undertaking my PhD in food policy in the charitable food relief sector, specifically investigating the factors (supply, demand and capacity) that affect the introduction of nutrition policy and in turn, affect the sector's ability to achieve equity, effectiveness and efficiency.

I need a graphic device that incorporates this central idea of Equity, Effectiveness and Efficiency, and how the factors of supply, demand and capacity interact. There are sub-factors within supply (1-6), demand (7-10) and capacity (11 - 15). All these details are shown in the attached figure (Basic figure_Eq Effec Effic and factors.jpg)

This figure (Basic figure_Eq Effec Effic and factors.jpg) contains all the information I need in a graphic but I need something that is more visually appealing, and that can link the ideas in a format other than a table. The final graphic will outline how the food relief sector balances the core objectives of equity, effectiveness and efficiency with the factors (and sub-factors) of supply, demand and capacity.

```html
<!DOCTYPE html>
<html lang="en">
<head>
<meta charset="utf-8">
<title>Factors Affecting Introduction of Nutrition Policy</title>
<link href="https://fonts.googleapis.com/css2?family=Oswald:wght@500;600&family=Lato:ital,wght@0,400;0,700;1,400&display=swap" rel="stylesheet">
<style>
  :root{
    --backdrop:#262626;
    --card:#ffffff;
    --header-band:#dcecd5;
    --pale:#e2efdc;
    --lime:#8dbb2c;
    --lime-fill:#a6c93c;
    --mid-green:#1f9a4a;
    --deep-green:#0b4c29;
    --title-green:#135a2c;
    --ink:#222;
    --dots:#777;
  }
  html,body{margin:0;padding:0;width:1200px;height:1178px;overflow:hidden;background:var(--backdrop);}
  .infographic{display:block;width:1200px;height:1178px;}
  .display{font-family:'Oswald',sans-serif;font-weight:600;}
  .label{font-family:'Lato',sans-serif;font-weight:700;font-size:11.5px;fill:var(--lime);}
  .bullet-text{font-family:'Lato',sans-serif;font-size:11.5px;fill:var(--ink);}
  .list-text{font-family:'Lato',sans-serif;font-size:11.5px;fill:#fff;}
  .credit{font-family:'Lato',sans-serif;font-style:italic;font-size:10.5px;fill:var(--ink);}
  .leader{stroke:var(--dots);stroke-width:1.3;stroke-dasharray:1.5 2.5;fill:none;}
  .node{fill:var(--lime-fill);stroke:#fff;stroke-width:2;}
  .node-icon{fill:none;stroke:#fff;stroke-width:1.6;stroke-linecap:round;stroke-linejoin:round;}
  .badge{fill:var(--pale);stroke:#fff;stroke-width:4;}
</style>
</head>
<body>
<svg class="infographic" viewBox="0 0 1019 1000" xmlns="http://www.w3.org/2000/svg">
  <defs>
    <filter id="soft-shadow" x="-30%" y="-30%" width="160%" height="170%">
      <feDropShadow dx="0" dy="3" stdDeviation="3" flood-color="#000" flood-opacity="0.22"/>
    </filter>
  </defs>

  <!-- card -->
  <rect x="75" y="145" width="878" height="680" fill="var(--card)"/>
  <rect class="footer-bar" x="75" y="815" width="878" height="10" fill="var(--lime-fill)"/>

  <!-- header -->
  <rect class="header-band" x="75" y="145" width="878" height="95" fill="var(--header-band)" filter="url(#soft-shadow)"/>
  <text class="display" x="514" y="186" text-anchor="middle" font-size="34" fill="var(--title-green)">FACTORS AFFECTING INTRODUCTION OF</text>
  <text class="display" x="514" y="229" text-anchor="middle" font-size="44" fill="var(--lime)">NUTRITION POLICY</text>
  <g class="leaf-mark" fill="var(--lime)">
    <path d="M344 226 C332 220 332 206 340 198 C346 208 348 218 344 226Z"/>
    <path d="M349 226 C361 220 361 206 353 198 C347 208 345 218 349 226Z"/>
    <path d="M684 226 C672 220 672 206 680 198 C686 208 688 218 684 226Z"/>
    <path d="M689 226 C701 220 701 206 693 198 C687 208 685 218 689 226Z"/>
  </g>

  <!-- pyramid -->
  <g class="pyramid">
    <polygon points="514,300 384,510 645,510" fill="var(--lime-fill)"/>
    <polygon points="384,510 518,510 518,765 225,765" fill="var(--mid-green)"/>
    <polygon points="518,510 645,510 805,765 518,765" fill="var(--deep-green)"/>
  </g>

  <!-- capacity nodes -->
  <g class="capacity-nodes">
    <line class="leader" x1="535" y1="386" x2="692" y2="386"/>
    <line class="leader" x1="535" y1="429" x2="692" y2="429"/>
    <line class="leader" x1="342" y1="463" x2="498" y2="463"/>
    <line class="leader" x1="342" y1="499" x2="454" y2="499"/>
    <line class="leader" x1="580" y1="499" x2="692" y2="499"/>

    <circle class="node" cx="517" cy="386" r="17"/>
    <g class="node-icon"><path d="M508 396 V380 L517 375 L526 380 V396"/><path d="M512 396 V386 H522 V396"/><path d="M512 390 H522"/></g>

    <circle class="node" cx="517" cy="429" r="17"/>
    <g class="node-icon"><circle cx="517" cy="429" r="5"/><circle cx="517" cy="419" r="2.2"/><circle cx="507" cy="433" r="2.2"/><circle cx="527" cy="433" r="2.2"/></g>

    <circle class="node" cx="517" cy="472" r="17"/>
    <g class="node-icon"><circle cx="517" cy="467" r="3"/><circle cx="509" cy="471" r="2.4"/><circle cx="525" cy="471" r="2.4"/><path d="M511 481 C511 474 523 474 523 481"/><path d="M504 480 C504 476 508 475 510 476"/><path d="M530 480 C530 476 526 475 524 476"/></g>

    <circle class="node" cx="472" cy="488" r="17"/>
    <text x="472" y="494" text-anchor="middle" font-family="Lato, sans-serif" font-weight="700" font-size="17" fill="#fff">$</text>

    <circle class="node" cx="562" cy="488" r="17"/>
    <g class="node-icon" fill="#fff"><rect x="551" y="482" width="14" height="9" fill="#fff" stroke="none"/><path d="M565 484 H570 L573 488 V491 H565Z" fill="#fff" stroke="none"/><circle cx="555" cy="493" r="1.8"/><circle cx="569" cy="493" r="1.8"/></g>
  </g>

  <!-- capacity badge -->
  <circle class="badge" cx="514" cy="307" r="40" filter="url(#soft-shadow)"/>
  <g class="badge-icon" fill="none" stroke="var(--mid-green)" stroke-width="3" stroke-linecap="round">
    <path d="M489 325 A25 25 0 0 1 539 325"/>
    <path d="M489 325 H539"/>
    <circle cx="514" cy="314" r="6"/>
    <path d="M514 300 V278"/>
    <path d="M506 286 L514 277 L522 286"/>
  </g>
  <text class="display" x="568" y="320" font-size="25" fill="var(--lime)">CAPACITY</text>

  <!-- capacity labels -->
  <text class="label" x="698" y="389">STORAGE</text>
  <text class="bullet-text" x="698" y="402"><tspan fill="var(--lime)">•</tspan> Cold  <tspan fill="var(--lime)">•</tspan> Warehouse</text>
  <text class="label" x="698" y="428">WORKFORCE</text>
  <text class="bullet-text" x="698" y="442"><tspan fill="var(--lime)">•</tspan> Volunteers  <tspan fill="var(--lime)">•</tspan> Collaboration</text>
  <text class="bullet-text" x="698" y="455"><tspan fill="var(--lime)">•</tspan> Expertise &amp; Training</text>
  <text class="bullet-text" x="698" y="468"><tspan fill="var(--lime)">•</tspan> Attitudes &amp; Beliefs</text>
  <text class="bullet-text" x="698" y="482"><tspan fill="var(--lime)">•</tspan> Executive Support</text>
  <text class="label" x="698" y="502">TRANSPORTATION</text>
  <text class="label" x="337" y="467" text-anchor="end">EXTERNAL</text>
  <text class="label" x="337" y="481" text-anchor="end">STAKEHOLDERS</text>
  <text class="label" x="337" y="503" text-anchor="end">BUDGET</text>

  <!-- core objectives -->
  <circle class="badge" cx="516" cy="583" r="80" stroke-width="5" filter="url(#soft-shadow)"/>
  <text class="display" x="516" y="566" text-anchor="middle" font-size="25" fill="var(--deep-green)">EQUITY</text>
  <text class="display" x="516" y="593" text-anchor="middle" font-size="25" fill="var(--mid-green)">EFFECTIVENESS</text>
  <text class="display" x="516" y="620" text-anchor="middle" font-size="25" fill="var(--deep-green)">EFFICIENCY</text>

  <!-- supply list -->
  <g class="list-text">
    <text x="325" y="679">• Uncertain MaterialSupply</text>
    <text x="325" y="692">• Uncertain Monetary Supply</text>
    <text x="325" y="706">• Limited Food Supply</text>
    <text x="325" y="719">• Perishability</text>
    <text x="325" y="732">• Donor Constraints</text>
    <text x="325" y="746">• Donor Relationships</text>
  </g>
  <!-- demand list -->
  <g class="list-text">
    <text x="575" y="679">• Uncertain Demand</text>
    <text x="575" y="692">• Limited Demand Visibility</text>
    <text x="575" y="706">• Client Choice</text>
    <text x="575" y="719">• Food Wastage</text>
  </g>

  <!-- supply badge -->
  <circle class="badge" cx="246" cy="746" r="42" filter="url(#soft-shadow)"/>
  <g fill="none" stroke="var(--mid-green)" stroke-width="2.6" stroke-linejoin="round">
    <circle cx="246" cy="746" r="22"/>
    <path d="M246 733 L258 740 V753 L246 760 L234 753 V740Z"/>
    <path d="M234 740 L246 747 L258 740 M246 747 V760"/>
  </g>
  <g fill="var(--mid-green)">
    <circle cx="246" cy="724" r="4.5"/><circle cx="246" cy="768" r="4.5"/>
    <circle cx="227" cy="735" r="4.5"/><circle cx="265" cy="735" r="4.5"/>
    <circle cx="227" cy="757" r="4.5"/><circle cx="265" cy="757" r="4.5"/>
  </g>
  <text class="display" x="122" y="757" font-size="25" fill="var(--mid-green)">SUPPLY</text>

  <!-- demand badge -->
  <circle class="badge" cx="780" cy="746" r="42" filter="url(#soft-shadow)"/>
  <g fill="none" stroke="var(--deep-green)" stroke-width="2.6" stroke-linecap="round" stroke-linejoin="round">
    <path d="M760 726 V767 H802"/>
    <path d="M764 760 L773 744 L781 752 L790 737"/>
    <circle cx="790" cy="751" r="7"/>
    <path d="M795 756 L801 762"/>
    <path d="M787 727 H801 M791 733 H801"/>
  </g>
  <text class="display" x="828" y="757" font-size="25" fill="var(--deep-green)">DEMAND</text>

  <text class="credit" x="518" y="805" text-anchor="middle">Icons by Leafline, Sprigwork from Iconfield.com</text>
</svg>
</body>
</html>
```